依頼詳細
駅前でチラシを配り集客の確保
記載項目
イタリアンダイニング VELMORA(ヴェルモーラ)東京都中野区中野3−17−9 4F 簡単なMAP
TEL03ー6454−0255 中野に本格イラリアンダイニング オープン!!
オープニング STAFF募集中

サイズ
A5
ページ数
片面
希望イメージ
シンプル 複雑
単色 カラフル
暗い 明るい
日常 高級
遊び心 厳粛
未来的 伝統的
女性的 男性的
希望する色
赤系
納品ファイル
• イラストレーター形式 (.ai)
補足説明
チラシに使う料理ですが4品位
パスタ、ピザ、肉料理、アヒージョなど無料サンプル画像を使って下さい
カジュアル イタリアンダイニング
営業時間 18時から5時
デリカポルト出前出来ます。
追加して下さい
画像を追加して下さい。
メニュー画像

全体のイメージ

チラシのデザイン有難う御座います。

```html
<!DOCTYPE html>
<html lang="ja">
<head>
<meta charset="utf-8">
<title>VELMORA オープン</title>
<link href="https://fonts.googleapis.com/css2?family=Noto+Sans+JP:wght@400;700;900&family=Anton&family=Pinyon+Script&family=Playfair+Display:ital,wght@0,700;1,400&display=swap" rel="stylesheet">
<style>
  :root {
    --paper: #eeebe3;
    --ink: #1d1a18;
    --red: #d22e26;
    --brown: #4e3425;
    --grey: #6c6760;
    --rule: #bdb6aa;
    --delivery: #2f2f2f;
  }
  * { box-sizing: border-box; margin: 0; padding: 0; }
  html, body { width: 844px; height: 1200px; overflow: hidden; background: var(--paper); }
  .flyer {
    position: relative; width: 844px; height: 1200px; overflow: hidden;
    background: var(--paper); font-family: "Noto Sans JP", sans-serif; color: var(--ink);
  }
  .photo { position: absolute; }
  .photo--ajillo { left: -20px; top: -30px; width: 270px; height: 340px; border-radius: 0 0 50% 0; background: radial-gradient(circle at 45% 45%, #f2c46a, #d86a3a 45%, #7d8f3c 75%, #5d4a2e); }
  .photo--pizza { right: -40px; top: -50px; width: 290px; height: 290px; border-radius: 50%; background: radial-gradient(circle, #e9b35a, #c7532e 55%, #9b6a3a 80%); }
  .photo--pasta { left: 14px; top: 410px; width: 285px; height: 285px; border-radius: 50%; background: radial-gradient(circle at 50% 45%, #e79a3c, #c44a24 50%, #4a3326 85%); }
  .photo--steak { right: 70px; top: 410px; width: 220px; height: 220px; border-radius: 50%; background: radial-gradient(circle at 50% 50%, #a44a34, #6f9a3e 55%, #e8e2d4 80%); }
  .photo--shrimp { right: -30px; top: 600px; width: 270px; height: 270px; border-radius: 50%; background: radial-gradient(circle, #f0a070, #e0c890 50%, #f4efe6 80%); }
  .photo--dish { left: 20px; top: 1075px; width: 250px; height: 110px; border-radius: 8px; background: linear-gradient(135deg, #6a4a30, #c0843e 55%, #4a5a2a); }

  .script-label { position: absolute; font-family: "Pinyon Script", cursive; color: var(--grey); font-size: 30px; }
  .script-label--ajillo { left: 18px; top: 320px; }
  .script-label--pizza { right: 110px; top: 10px; }
  .script-label--pasta { right: 30px; top: 860px; font-size: 40px; }

  .headline { position: absolute; left: 222px; top: 20px; width: 420px; text-align: center; }
  .headline__tag { display: inline-block; background: var(--red); color: #fff; font-weight: 900; font-size: 28px; padding: 2px 18px; border-radius: 10px; position: relative; }
  .headline__tag::after { content: ""; position: absolute; left: 50%; bottom: -12px; margin-left: -8px; border: 8px solid transparent; border-top-color: var(--red); border-bottom: 0; border-top-width: 12px; }
  .headline__lead { margin-top: 20px; font-weight: 900; font-size: 37px; line-height: 1.25; letter-spacing: 1px; white-space: nowrap; }
  .headline__brand { font-family: "Anton", sans-serif; color: var(--red); font-size: 72px; line-height: 1.05; letter-spacing: 2px; margin-top: 4px; }
  .headline__kana { font-size: 15px; font-weight: 700; margin-left: 150px; }

  .open-word { position: absolute; left: 290px; top: 325px; font-family: "Pinyon Script", cursive; font-size: 128px; color: var(--brown); line-height: 1; }

  .recruit { position: absolute; left: 655px; top: 240px; width: 160px; height: 160px; border-radius: 50%; background: var(--red); color: #fff; text-align: center; font-weight: 900; display: flex; flex-direction: column; justify-content: center; font-size: 19px; line-height: 1.3; }
  .recruit__staff { font-family: "Anton", sans-serif; font-size: 34px; font-weight: 400; letter-spacing: 1px; }

  .map { position: absolute; left: 315px; top: 478px; width: 235px; height: 222px; background: #e4dfd4; border: 1px solid var(--rule); }

  .menu { position: absolute; top: 712px; font-size: 10px; color: var(--ink); }
  .menu--left { left: 22px; width: 260px; }
  .menu--mid { left: 298px; width: 250px; }
  .menu__heading { font-family: "Playfair Display", serif; font-weight: 700; font-size: 13px; border-bottom: 1px solid var(--rule); padding-bottom: 2px; margin: 8px 0 4px; }
  .menu__list { list-style: none; columns: 2; column-gap: 10px; }
  .menu--mid .menu__list { columns: 1; }
  .menu__list li { line-height: 1.75; display: flex; justify-content: space-between; }

  .shop { position: absolute; left: 566px; top: 915px; width: 260px; }
  .shop__sub { font-family: "Playfair Display", serif; font-style: italic; font-size: 16px; text-align: center; }
  .shop__name { font-family: "Anton", sans-serif; font-size: 40px; text-align: center; letter-spacing: 2px; line-height: 1.1; }
  .shop__info { font-size: 10px; margin-top: 10px; line-height: 1.5; white-space: nowrap; }
  .shop__tel { color: var(--red); font-family: "Anton", sans-serif; font-size: 32px; margin-top: 4px; white-space: nowrap; }
  .shop__tel small { font-family: "Noto Sans JP", sans-serif; font-size: 14px; font-weight: 700; }
  .shop__delivery { font-weight: 700; font-size: 13px; margin-top: 2px; }
  .delivery-badge { position: absolute; right: 0; top: 155px; width: 46px; height: 46px; background: var(--delivery); border-radius: 4px; }
</style>
</head>
<body>
<main class="flyer">
  <div class="photo photo--ajillo" role="img" aria-label="アヒージョの料理写真"></div>
  <div class="photo photo--pizza" role="img" aria-label="ピザの料理写真"></div>
  <span class="script-label script-label--ajillo">Ajillo</span>
  <span class="script-label script-label--pizza">Pizza</span>

  <header class="headline">
    <span class="headline__tag">中野に</span>
    <p class="headline__lead">本格カジュアル<br>イタリアンダイニング</p>
    <h1 class="headline__brand">VELMORA</h1>
    <p class="headline__kana">ヴェルモーラ</p>
  </header>

  <div class="recruit">
    <span>オープニング</span>
    <span class="recruit__staff">STAFF</span>
    <span>募集中!</span>
  </div>

  <p class="open-word">Open</p>

  <div class="photo photo--pasta" role="img" aria-label="トマトパスタの料理写真"></div>
  <div class="map" role="img" aria-label="中野駅北口から店舗までの簡単な地図(中野セントラル・ナカノ通り・チキン亭付近、ヴェルモーラ4F)"></div>
  <div class="photo photo--steak" role="img" aria-label="肉料理とサラダの写真"></div>
  <div class="photo photo--shrimp" role="img" aria-label="海老のパスタの写真"></div>
  <span class="script-label script-label--pasta">Pasta</span>

  <section class="menu menu--left">
    <h2 class="menu__heading">Tapas</h2>
    <ul class="menu__list">
      <li><span>オリーブ</span><span>380</span></li>
      <li><span>生ハム</span><span>580</span></li>
      <li><span>チーズ盛り</span><span>680</span></li>
      <li><span>ピクルス</span><span>380</span></li>
      <li><span>ポテト</span><span>480</span></li>
      <li><span>バゲット</span><span>300</span></li>
    </ul>
    <h2 class="menu__heading">A La Carte</h2>
    <ul class="menu__list">
      <li><span>カルパッチョ</span><span>780</span></li>
      <li><span>アヒージョ</span><span>680</span></li>
      <li><span>カプレーゼ</span><span>680</span></li>
      <li><span>シーザーサラダ</span><span>780</span></li>
      <li><span>フリット</span><span>580</span></li>
      <li><span>ブルスケッタ</span><span>480</span></li>
      <li><span>キッシュ</span><span>580</span></li>
      <li><span>パテ</span><span>680</span></li>
    </ul>
  </section>

  <section class="menu menu--mid">
    <h2 class="menu__heading">Pizza</h2>
    <ul class="menu__list">
      <li><span>マルゲリータ</span><span>980</span></li>
      <li><span>クアトロフォルマッジ</span><span>1,180</span></li>
      <li><span>マリナーラ</span><span>880</span></li>
    </ul>
    <h2 class="menu__heading">Pasta</h2>
    <ul class="menu__list">
      <li><span>ペスカトーレ</span><span>1,280</span></li>
      <li><span>カルボナーラ</span><span>1,080</span></li>
      <li><span>ボロネーゼ</span><span>1,080</span></li>
    </ul>
    <h2 class="menu__heading">Main</h2>
    <ul class="menu__list">
      <li><span>牛ステーキ</span><span>1,980</span></li>
      <li><span>鶏のロースト</span><span>1,480</span></li>
    </ul>
    <h2 class="menu__heading">Dessert</h2>
    <ul class="menu__list">
      <li><span>ティラミス</span><span>480</span></li>
      <li><span>パンナコッタ</span><span>480</span></li>
    </ul>
  </section>

  <div class="photo photo--dish" role="img" aria-label="料理の盛り合わせ写真"></div>

  <footer class="shop">
    <p class="shop__sub">Casual Dining</p>
    <p class="shop__name">VELMORA</p>
    <p class="shop__info">東京都中野区中野3−17−9 4F 営業時間18時〜翌5時</p>
    <p class="shop__tel"><small>tel.</small>03ー5827−3916</p>
    <p class="shop__delivery">デリカポルト出前出来ます。</p>
    <div class="delivery-badge" aria-hidden="true"></div>
  </footer>
</main>
</body>
</html>
```